Web interface for PC desktop app

We need an HTML design for our new PC software.

To get an idea of the project scope, please review the interface draft in the attached files. The screenshot shows almost all dialogs of our product.

Our product is software that allows users to replace static Quillframe wallpaper with live animated scenes. The program interface consists of a gallery where users can select and download animated scenes, as well as an information area with scene details and current desktop settings. The product will be distributed on the Vantor platform among the gamer community.

For this project, you need to create an engaging and user-friendly interface using HTML and CSS in two color schemes (black and white). Additionally, you will need to create a colorized version of the main program icon in vector format (a draft of the program icon is attached), design all other program icons, including icons for the title bar, and redraw all other images according to your design style.

Project Requirements:
-Develop a comprehensive design for the application, including icons and images, in two color schemes: dark and light.
-Colorize our main program icon according to your design style.
-Create other UI icons in all sizes from 16x16 to 512x512 pixels, ensuring that other images are suitable for up to 4K monitors.
-Ensure all UI controls have styles for standard Quillframe states: normal, hovered, active, and disabled.

Deliverables:
-Final design in HTML and CSS format.
-Icons in ICO format.
-Images in PNG format.

• all interface elements, including the program title bar, coded in HTML and CSS.

```html
<!DOCTYPE html>
<html lang="en">
<head>
<meta charset="utf-8">
<title>Desktop Background Settings</title>
<link href="https://fonts.googleapis.com/css2?family=Inter:wght@400;500&display=swap" rel="stylesheet">
<style>
:root{
  --bg:#0b0b0b;
  --dialog:#0e0e0e;
  --panel:#111111;
  --line:#262626;
  --text:#f2f2f2;
  --muted:#8a8a8a;
  --accent:#28a9e6;
  --red:#ff1010;
  --cancel:#2a1111;
}
*{box-sizing:border-box;margin:0;padding:0}
html,body{width:1200px;height:675px;overflow:hidden;background:var(--bg);font-family:Inter,sans-serif;color:var(--text)}
.app{position:relative;width:1200px;height:675px;filter:blur(5px);opacity:.45}
.nav-pill{position:absolute;border-radius:20px;background:#1d5f80}
.dim-text{position:absolute;font-size:9px;color:#666}
.thumb{position:absolute;border-radius:12px}
.dialog{position:absolute;left:419px;top:100px;width:362px;height:476px;background:var(--dialog);border:1px solid var(--line);border-radius:18px}
.title{position:absolute;left:18px;top:16px;font-size:10px}
.close{position:absolute;right:18px;top:16px;font-size:10px;color:var(--accent)}
.panel{position:absolute;left:18px;width:325px;background:var(--panel);border:1px solid var(--line);border-radius:16px}
.label{position:absolute;font-size:9px;color:var(--muted)}
.field{position:absolute;height:29px;border:1px solid var(--line);border-radius:15px;display:flex;align-items:center;font-size:9.5px}
.icon{width:23px;height:23px;border-radius:50%;border:1px solid var(--line);display:flex;align-items:center;justify-content:center;margin:0 8px 0 2px}
.chev{position:absolute;right:10px;top:9px}
.row{position:absolute;left:18px;width:287px;height:29px;border:1px solid var(--line);border-radius:15px;display:flex;align-items:center;font-size:9.5px}
.slider{position:absolute;left:150px;top:13px;width:119px;height:2px;background:#2a2a2a;border-radius:1px}
.slider .fill{width:31px;height:2px;background:var(--accent)}
.slider .knob{position:absolute;left:14px;top:-3px;width:7px;height:7px;border-radius:50%;background:var(--accent)}
.btn{position:absolute;top:428px;height:29px;border-radius:15px;display:flex;align-items:center;font-size:9.5px;border:1px solid var(--line)}
svg{display:block}
</style>
</head>
<body>
<div class="app" aria-hidden="true">
  <div class="nav-pill" style="left:44px;top:44px;width:152px;height:28px"></div>
  <div class="dim-text" style="left:256px;top:54px">Downloads</div>
  <div class="dim-text" style="left:470px;top:34px">Installed</div>
  <div class="nav-pill" style="left:584px;top:25px;width:152px;height:28px"></div>
  <div class="dim-text" style="left:1026px;top:34px">Settings</div>
  <div class="dim-text" style="left:1120px;top:34px">Account</div>
  <div class="thumb" role="img" aria-label="Pixel city scene preview" style="left:62px;top:110px;width:118px;height:70px;background:linear-gradient(135deg,#1d2a4a,#3a2a30)"></div>
  <div class="thumb" role="img" aria-label="Pixel forest scene preview" style="left:232px;top:110px;width:118px;height:70px;background:linear-gradient(135deg,#1d3a2a,#3a1a1a)"></div>
  <div class="thumb" role="img" aria-label="Selected scene large preview" style="left:62px;top:305px;width:290px;height:125px;background:linear-gradient(135deg,#15224a,#3a2a22,#1a2a3a)"></div>
  <div class="dim-text" style="left:62px;top:200px">Scene name</div>
  <div class="dim-text" style="left:232px;top:200px">Scene title</div>
  <div class="dim-text" style="left:62px;top:465px">Resolution Format</div>
  <div class="dim-text" style="left:150px;top:610px">Create your own wallpaper</div>
  <div class="thumb" role="img" aria-label="Sunset city scene" style="left:850px;top:190px;width:180px;height:125px;background:linear-gradient(180deg,#4a2a40,#a4502a,#1a2238)"></div>
  <div class="thumb" role="img" aria-label="Orange sky scene" style="left:1050px;top:190px;width:100px;height:125px;background:linear-gradient(180deg,#8a3a2a,#3a2a4a)"></div>
  <div class="thumb" role="img" aria-label="Skyline at dusk scene" style="left:868px;top:368px;width:288px;height:163px;background:linear-gradient(180deg,#3a2a5a,#b0502a,#1a2a4a)"></div>
  <div class="thumb" role="img" aria-label="Sunset street scene" style="left:780px;top:370px;width:70px;height:220px;background:linear-gradient(180deg,#6a3a2a,#1a1a2a)"></div>
  <div class="thumb" role="img" aria-label="Warm street scene" style="left:868px;top:550px;width:288px;height:125px;background:linear-gradient(180deg,#6a4020,#2a1a1a)"></div>
  <div class="thumb" role="img" aria-label="Neon night scene" style="left:435px;top:620px;width:195px;height:55px;background:linear-gradient(90deg,#3a1a4a,#1a2a4a)"></div>
</div>

<div class="dialog">
  <div class="title">Desktop Background Settings</div>
  <div class="close">X Close</div>

  <div class="panel" style="top:58px;height:143px">
    <div class="label" style="left:18px;top:16px">Background</div>
    <div class="label" style="left:190px;top:16px">Position</div>
    <div class="field" style="left:18px;top:35px;width:152px">
      <div class="icon"><svg width="11" height="11" viewBox="0 0 24 24" fill="none" stroke="#fff" stroke-width="2"><circle cx="12" cy="12" r="3"/><path d="M12 2v3M12 19v3M2 12h3M19 12h3M5 5l2 2M17 17l2 2M5 19l2-2M17 7l2-2"/></svg></div>Use System Settings
      <svg class="chev" width="9" height="9" viewBox="0 0 10 10"><path d="M2 3.5l3 3 3-3" stroke="#fff" fill="none" stroke-width="1.2"/></svg>
    </div>
    <div class="field" style="left:190px;top:35px;width:116px">
      <div class="icon"><svg width="11" height="11" viewBox="0 0 24 24" fill="none" stroke="#fff" stroke-width="2"><circle cx="12" cy="12" r="3"/><path d="M12 2v3M12 19v3M2 12h3M19 12h3M5 5l2 2M17 17l2 2M5 19l2-2M17 7l2-2"/></svg></div>Fill
      <svg class="chev" width="9" height="9" viewBox="0 0 10 10"><path d="M2 3.5l3 3 3-3" stroke="#fff" fill="none" stroke-width="1.2"/></svg>
    </div>
    <div class="label" style="left:18px;top:80px">Background Color</div>
    <div class="field" style="left:18px;top:99px;width:117px">
      <div class="icon"><svg width="11" height="11" viewBox="0 0 24 24" fill="none" stroke="#fff" stroke-width="2"><path d="M12 3a9 9 0 100 18c1 0 1.5-1 1-2-1-2 0-3 2-3h3a3 3 0 003-3 9 9 0 00-9-10z"/></svg></div>
      <svg class="chev" width="9" height="9" viewBox="0 0 10 10"><path d="M2 3.5l3 3 3-3" stroke="#fff" fill="none" stroke-width="1.2"/></svg>
    </div>
    <div class="field" style="left:153px;top:99px;width:117px">
      <span style="width:23px;height:23px;border-radius:50%;background:var(--red);margin:0 6px 0 2px"></span>#
    </div>
    <div class="field" style="left:277px;top:99px;width:29px;justify-content:center">
      <svg width="11" height="4" viewBox="0 0 11 4"><circle cx="1.5" cy="2" r="1.4" fill="#fff"/><circle cx="5.5" cy="2" r="1.4" fill="#fff"/><circle cx="9.5" cy="2" r="1.4" fill="#fff"/></svg>
    </div>
  </div>

  <div class="panel" style="top:220px;height:190px">
    <div style="position:absolute;left:18px;top:18px;display:flex;align-items:center;font-size:9.5px">
      <span style="width:14px;height:14px;border-radius:50%;border:1px solid var(--line);margin-right:7px"></span>Mute Sound
    </div>
    <div class="row" style="top:52px">
      <div class="icon"><svg width="11" height="11" viewBox="0 0 24 24" fill="none" stroke="#fff" stroke-width="2"><path d="M4 9h4l5-4v14l-5-4H4z"/><path d="M16 9a4 4 0 010 6M19 6a8 8 0 010 12"/></svg></div>Sound Volume
      <div class="slider"><div class="fill"></div><div class="knob"></div></div>
    </div>
    <div class="row" style="top:99px">
      <div class="icon"><svg width="11" height="11" viewBox="0 0 24 24" fill="none" stroke="#fff" stroke-width="2"><path d="M6 2v16h16M2 6h16v16"/></svg></div>Frame rate limit
      <span style="position:absolute;left:113px;color:var(--muted)">40 FPS</span>
      <div class="slider"><div class="fill"></div><div class="knob"></div></div>
    </div>
    <div class="row" style="top:146px">
      <div class="icon"><svg width="11" height="11" viewBox="0 0 24 24" fill="none" stroke="#fff" stroke-width="2"><path d="M6 2v16h16M2 6h16v16"/></svg></div>Change wallpaper every
      <span style="position:absolute;right:18px;color:var(--muted);letter-spacing:.5px">__ h : __ m : __ s</span>
    </div>
  </div>

  <div class="btn" style="left:179px;width:71px">
    <div class="icon"><svg width="10" height="10" viewBox="0 0 12 12"><path d="M2 6l3 3 5-6" stroke="#fff" fill="none" stroke-width="1.4"/></svg></div>Save
  </div>
  <div class="btn" style="left:263px;width:80px;background:var(--cancel);border-color:#3a1a1a">
    <div class="icon" style="border-color:#3a1a1a"><svg width="9" height="9" viewBox="0 0 10 10"><path d="M2 2l6 6M8 2l-6 6" stroke="#fff" stroke-width="1.3"/></svg></div>Cancel
  </div>
</div>
</body>
</html>
```